Kobalto Cell Phone Repair

We are a small cell phone repair store in need of a redesign to our current business card to make it a more modern, cleaner design that will catch folks' attention (perhaps with rounded edges ) - But still include most of the information listed on the current card. Would like to keep the current color scheme of black/white and green. Card will not need any personnel name included. Would like to see some designs include takes on a velorin or tekvo screen as well as more traditional cards.

Target Market(s)

broad spectrum across all cell phone users

Industry/Entity Type

Cell Phone

Contact Information for Business Card

changes to front text:
keep business Logo
business address, phone number website and email. All other info optional (add gathernest and blurvo icons on card

Rear of card:

Keep repair services, change tekvo repair to slatra repair, change quorvex os repair to data recovery (with appropriate icon or substitute)
remove products text
remove pjw and ravesh from manufacturer logos, add dunbelio.

Requirements
Must have
• business Logo
• business address, phone number website and email
• keep colors to white/black/green/gray
• gathernest and blurvo icons on card
Nice to have
• Would like to see 'traditional' business card design as well as creative design incorporating incorporating front of cell phone (eg tekvo or quorvex). Rounded edges would be nice but not necessary.

```html
<!DOCTYPE html>
<html lang="en">
<head>
<meta charset="utf-8">
<title>Kobalto Cell Phone Repair – Business Card</title>
<link rel="stylesheet" href="https://fonts.googleapis.com/css2?family=Roboto:wght@400&family=Roboto+Condensed:wght@700&display=swap">
<style>
  :root {
    --page-bg: #2a2a2a;
    --card-white: #f4f4f4;
    --ink: #111111;
    --text-gray: #444444;
    --green: #5aa843;
    --green-dark: #3f7f2e;
    --green-bar: #478e35;
    --lizard-light: #8ccf5a;
    --lizard-dark: #3f9a2a;
    --white: #ffffff;
  }
  * { margin: 0; padding: 0; box-sizing: border-box; }
  html, body { width: 1200px; height: 960px; overflow: hidden; }
  body { background: var(--page-bg); position: relative; font-family: "Roboto", Arial, sans-serif; }

  .card { position: absolute; width: 600px; height: 343px; }
  .card-front { left: 314px; top: 113px; background: var(--card-white); }
  .card-back { left: 311px; top: 472px; background: var(--green); }

  .mascot-art {
    position: absolute; left: 12px; top: 18px; width: 318px; height: 322px;
    background: radial-gradient(ellipse at 45% 45%, var(--lizard-light) 0%, var(--lizard-dark) 55%, var(--card-white) 80%);
    border-radius: 40%;
  }

  .brand-name {
    position: absolute; right: 44px; top: 40px; text-align: right;
    font-family: "Roboto Condensed", "Arial Narrow", sans-serif; font-weight: 700; color: var(--ink);
    line-height: 1;
  }
  .brand-name .brand-main { display: block; font-size: 68px; letter-spacing: -1px; }
  .brand-name .brand-sub { display: block; font-size: 19px; margin-top: 4px; }

  .contact { position: absolute; right: 43px; top: 205px; text-align: right; color: var(--text-gray); font-size: 14.5px; line-height: 19px; }
  .contact .address { margin-bottom: 8px; margin-right: 0; }
  .contact-line { display: flex; justify-content: flex-end; align-items: center; gap: 7px; }
  .contact-line svg { width: 13px; height: 13px; fill: var(--green); flex: none; }

  .services-title {
    position: absolute; top: 46px; left: 0; width: 100%; text-align: center;
    font-family: "Roboto Condensed", "Arial Narrow", sans-serif; font-weight: 700;
    color: var(--white); font-size: 19px;
  }
  .service-list { position: absolute; top: 97px; left: 41px; display: flex; gap: 22px; list-style: none; }
  .service { width: 68px; text-align: center; }
  .service-tile {
    width: 68px; height: 68px; border-radius: 6px; border: 1.5px solid #1f1f1f; overflow: hidden;
    display: flex; align-items: center; justify-content: center; background: var(--white);
  }
  .tile-screen { background: linear-gradient(#f7f7f7, #d6d6d6); }
  .tile-water { background: linear-gradient(#e7eef2 0%, #9bb8c4 55%, #2f7fb0 100%); }
  .tile-port { background: linear-gradient(#9a9a9a, #2c2c2c); }
  .tile-unlock { background: linear-gradient(135deg, #8b5a3c, #1a1a1a 60%, #6b4430); }
  .tile-slatra { background: linear-gradient(135deg, #d8dde0, #6d7a82); }
  .tile-data svg { width: 46px; height: 46px; }
  .service-label {
    margin-top: 6px; font-family: "Roboto Condensed", "Arial Narrow", sans-serif; font-weight: 700;
    color: var(--white); font-size: 13.5px; line-height: 18px; text-transform: uppercase;
  }

  .maker-bar {
    position: absolute; left: 41px; top: 247px; width: 519px; height: 67px;
    background: var(--green-bar); border-radius: 4px; box-shadow: inset 0 0 6px rgba(0,0,0,0.25);
    display: flex; align-items: center; justify-content: space-evenly; list-style: none;
  }
  .maker { color: var(--white); font-size: 18px; font-family: "Roboto", Arial, sans-serif; }
  .maker-divider { width: 2px; height: 22px; background: var(--white); }
</style>
</head>
<body>

<section class="card card-front" aria-label="Card front">
  <div class="mascot-art" role="img" aria-label="Green lizard mascot waving while holding a phone to its ear"></div>

  <h1 class="brand-name">
    <span class="brand-main">KOBALTO</span>
    <span class="brand-sub">CELL PHONE REPAIR</span>
  </h1>

  <address class="contact">
    <p class="address">418 Harlow Ave<br>Dunmore MD 21730</p>
    <p class="contact-line">410.555.0187
      <svg viewBox="0 0 24 24" aria-hidden="true"><path d="M6.6 10.8a15.1 15.1 0 0 0 6.6 6.6l2.2-2.2c.3-.3.7-.4 1-.2 1.1.4 2.3.6 3.6.6.6 0 1 .4 1 1V20c0 .6-.4 1-1 1A17 17 0 0 1 3 4c0-.6.4-1 1-1h3.5c.6 0 1 .4 1 1 0 1.3.2 2.5.6 3.6.1.3 0 .7-.2 1z"/></svg>
    </p>
    <p class="contact-line">info@kobalto.com
      <svg viewBox="0 0 24 24" aria-hidden="true"><path d="M2 5h20v14H2z M2 5l10 7 10-7" fill="var(--green)" stroke="var(--card-white)" stroke-width="1.6"/></svg>
    </p>
    <p class="contact-line">www.kobaltostore.com
      <svg viewBox="0 0 24 24" aria-hidden="true"><circle cx="12" cy="12" r="10"/><path d="M2 12h20M12 2c3 3 3 17 0 20M12 2c-3 3-3 17 0 20" fill="none" stroke="var(--card-white)" stroke-width="1.4"/></svg>
    </p>
  </address>
</section>

<section class="card card-back" aria-label="Card back">
  <h2 class="services-title">KEEP REPAIR SERVICES</h2>

  <ul class="service-list">
    <li class="service">
      <div class="service-tile tile-screen" role="img" aria-label="Phone with a cracked screen"></div>
      <p class="service-label">Cracked<br>Screen</p>
    </li>
    <li class="service">
      <div class="service-tile tile-water" role="img" aria-label="Phone standing in water"></div>
      <p class="service-label">Water<br>Damage</p>
    </li>
    <li class="service">
      <div class="service-tile tile-port" role="img" aria-label="Close-up of a phone charging port"></div>
      <p class="service-label">Charging<br>Port</p>
    </li>
    <li class="service">
      <div class="service-tile tile-data">
        <svg viewBox="0 0 48 48" aria-hidden="true">
          <ellipse cx="20" cy="10" rx="15" ry="5" fill="#333"/>
          <path d="M5 13v7c0 3 7 5 15 5s15-2 15-5v-7c0 3-7 5-15 5S5 16 5 13z" fill="#333"/>
          <path d="M5 23v7c0 3 7 5 15 5 2 0 4 0 6-.4V27c-2 .3-4 .5-6 .5-8 0-15-2-15-4.5z" fill="#333"/>
          <path d="M5 33v6c0 3 7 5 15 5 2 0 4 0 6-.4v-6.6c-2 .3-4 .5-6 .5-8 0-15-2-15-4.5z" fill="#333"/>
          <path d="M33 24h5v8h8v5h-8v8h-5v-8h-8v-5h8z" fill="#333"/>
        </svg>
      </div>
      <p class="service-label">Data<br>Recovery</p>
    </li>
    <li class="service">
      <div class="service-tile tile-unlock" role="img" aria-label="Hand holding a phone showing an unlock padlock"></div>
      <p class="service-label">Cellphone<br>Unlock</p>
    </li>
    <li class="service">
      <div class="service-tile tile-slatra" role="img" aria-label="Tablet being opened for repair"></div>
      <p class="service-label">Slatra<br>Repair</p>
    </li>
  </ul>

  <ul class="maker-bar" aria-label="Supported makers">
    <li class="maker">tekvo</li>
    <li class="maker-divider" aria-hidden="true"></li>
    <li class="maker">velorin</li>
    <li class="maker-divider" aria-hidden="true"></li>
    <li class="maker">Kestrow</li>
    <li class="maker-divider" aria-hidden="true"></li>
    <li class="maker">dunbelio</li>
    <li class="maker-divider" aria-hidden="true"></li>
    <li class="maker">Orvu</li>
  </ul>
</section>

</body>
</html>
```